BRISK Study flyer

I need help designing a flyer for a research study that will include brain imaging in adolescents. The info is in the attached document. The study is called the Brain Rhythms In School Kids (BRISK) study. Ideally this would be returned as a document that I can edit in the future as we will have several new recruitment phases (different age groups, etc. I also would love to have a logo designed as part of this project, but I recognize that might be a separate design request.

```html
<!DOCTYPE html>
<html lang="en">
<head>
<meta charset="utf-8">
<title>BRISK Study Flyer</title>
<link rel="stylesheet" href="https://fonts.googleapis.com/css2?family=League+Gothic&family=Montserrat:wght@400;500;600;700&display=swap">
<style>
  :root {
    --navy-deep: #0a1029;
    --navy: #0f1838;
    --navy-band: #15204a;
    --purple: #8e6bd8;
    --purple-deep: #4b2c8f;
    --purple-band: #3a2478;
    --teal: #2fc0bd;
    --white: #ffffff;
    --ink: #1b1f3a;
    --muted: #c9cce0;
    --panel: #f5f6f9;
  }
  * { margin: 0; padding: 0; box-sizing: border-box; }
  html, body { width: 800px; height: 1200px; overflow: hidden; background: var(--navy-deep); }
  body { font-family: "Montserrat", sans-serif; color: var(--white); }
  .flyer { position: relative; width: 800px; height: 1200px; background: var(--navy-deep); overflow: hidden; }
  .abs { position: absolute; }

  .hero-photo {
    left: 258px; top: 0; width: 542px; height: 648px;
    background:
      radial-gradient(ellipse 40% 45% at 60% 40%, #6b5a55 0%, #3a3440 40%, transparent 75%),
      radial-gradient(ellipse 45% 40% at 85% 20%, #6f7fa8 0%, #2a3560 45%, transparent 80%),
      linear-gradient(180deg, #101a3e 0%, #0c1434 70%, var(--navy-deep) 100%);
  }
  .hero-fade { left: 0; top: 0; width: 520px; height: 648px;
    background: linear-gradient(90deg, var(--navy-deep) 55%, rgba(10,16,41,0) 100%); }

  .brand { left: 31px; top: 28px; display: flex; align-items: center; gap: 18px; }
  .brand-mark { width: 64px; height: 64px; border-radius: 50%; background: var(--purple); flex: none; }
  .brand-name { font-family: "Montserrat", sans-serif; font-weight: 500; font-size: 36px; letter-spacing: 14px; line-height: 1; }
  .brand-full { font-size: 10px; letter-spacing: 1.2px; margin-top: 8px; line-height: 1.5; text-transform: uppercase; width: 200px; }

  .headline { left: 34px; top: 112px; font-family: "League Gothic", sans-serif; font-weight: 400; font-size: 140px; line-height: 111px; text-transform: uppercase; letter-spacing: -1px; }
  .headline .accent { color: var(--purple); }
  .headline-rule { left: 39px; top: 574px; width: 61px; height: 2px; background: var(--teal); }
  .tagline { left: 41px; top: 584px; width: 270px; font-size: 15px; line-height: 18.5px; color: #e6e8f2; }

  .side-words { left: 758px; top: 262px; writing-mode: vertical-rl; font-size: 10px; letter-spacing: 3.5px; color: #dfe2f0; }

  .compensation { left: 593px; top: 412px; width: 168px; height: 168px; border-radius: 50%; background: var(--purple-deep); text-align: center; padding-top: 28px; }
  .compensation .label { font-size: 12px; font-weight: 500; letter-spacing: 1px; line-height: 17px; }
  .compensation .amount { font-size: 44px; font-weight: 600; line-height: 52px; }
  .comp-ring { left: 400px; top: 390px; width: 330px; height: 330px; border-radius: 50%; border: 1px solid rgba(255,255,255,.25); }

  .audience-band { left: 0; top: 648px; width: 800px; height: 94px; background: var(--navy-band); }
  .icon-ring { border: 1.5px solid var(--teal); border-radius: 50%; display: flex; align-items: center; justify-content: center; }
  .audience-icon { left: 37px; top: 656px; width: 78px; height: 78px; }
  .audience-q { left: 142px; top: 667px; font-size: 15.5px; font-weight: 500; letter-spacing: .8px; white-space: nowrap; }
  .audience-age { left: 141px; top: 686px; font-family: "League Gothic", sans-serif; font-size: 42px; line-height: 48px; color: var(--purple); letter-spacing: 1px; white-space: nowrap; }
  .band-divider { left: 398px; top: 668px; width: 1px; height: 56px; background: rgba(255,255,255,.25); }
  .audience-worry { left: 423px; top: 666px; font-size: 16.5px; font-weight: 500; letter-spacing: 1px; line-height: 21px; text-transform: uppercase; }
  .audience-worry .q { color: var(--teal); }

  .involve-panel { left: 0; top: 742px; width: 361px; height: 297px; background: var(--panel); clip-path: polygon(0 0, 361px 0, 309px 297px, 0 297px); }
  .involve-title { left: 37px; top: 760px; font-size: 14px; font-weight: 700; color: var(--ink); letter-spacing: .5px; }
  .step { left: 36px; display: flex; gap: 19px; width: 275px; }
  .step-icon { width: 58px; height: 58px; border-radius: 50%; flex: none; display: flex; align-items: center; justify-content: center; }
  .step-name { font-size: 12.5px; font-weight: 600; letter-spacing: .3px; text-transform: uppercase; }
  .step-text { font-size: 11px; line-height: 14px; color: var(--ink); }
  .step-rule { left: 113px; width: 192px; border-top: 1px dotted #b7bccd; }

  .eligible-title { left: 387px; top: 768px; font-size: 15.5px; font-weight: 500; color: var(--teal); letter-spacing: 1px; line-height: 20px; text-transform: uppercase; }
  .eligible-rule { left: 387px; top: 813px; width: 28px; height: 2px; background: var(--teal); }
  .criteria { left: 386px; top: 830px; list-style: none; width: 190px; }
  .criteria li { display: flex; gap: 10px; font-size: 13px; line-height: 18px; color: #eef0f7; margin-bottom: 20px; }
  .criteria svg { flex: none; margin-top: 1px; }

  .scan-image { left: 582px; top: 719px; width: 218px; height: 320px;
    background: radial-gradient(ellipse 55% 50% at 60% 45%, #7f8cb0 0%, #3a4670 45%, var(--navy) 85%); }

  .contact-band { left: 0; top: 1039px; width: 800px; height: 78px; background: linear-gradient(90deg, var(--purple-band) 0%, #2a1d62 55%, var(--navy-band) 100%); }
  .contact-icon { left: 38px; top: 1051px; width: 54px; height: 54px; border-color: var(--white); }
  .contact-copy { left: 115px; top: 1052px; }
  .contact-copy .a { font-size: 14px; font-weight: 500; letter-spacing: 1px; }
  .contact-copy .b { font-size: 17px; font-weight: 600; letter-spacing: 1px; color: var(--teal); }
  .contact-copy .c { font-size: 11.5px; }
  .contact-divider { left: 409px; top: 1052px; width: 1px; height: 52px; background: rgba(255,255,255,.3); }
  .contact-email { left: 453px; top: 1060px; font-size: 23px; font-weight: 500; }
  .email-rule { left: 453px; top: 1098px; width: 30px; height: 2px; background: var(--teal); }

  .footer { left: 0; top: 1117px; width: 800px; height: 83px; background: var(--navy-deep); }
  .institution { left: 47px; top: 1140px; display: flex; align-items: center; gap: 12px; }
  .institution-mark { width: 38px; height: 38px; border-radius: 50%; background: var(--white); }
  .institution-name { font-size: 17px; font-weight: 600; line-height: 19px; }
  .foot-divider { top: 1132px; width: 0; height: 54px; border-left: 1px dotted rgba(255,255,255,.35); }
  .foot-icon { width: 50px; height: 50px; }
  .foot-text { font-size: 10px; line-height: 13px; color: #dfe2ee; white-space: nowrap; }
</style>
</head>
<body>
<main class="flyer">
  <div class="abs hero-photo" role="img" aria-label="Portrait of a thoughtful teenager beside a blue-toned brain MRI scan"></div>
  <div class="abs hero-fade"></div>

  <header class="abs brand">
    <div class="brand-mark"></div>
    <div>
      <div class="brand-name">BRISK</div>
      <div class="brand-full">Brain Rhythms In School Kids Study</div>
    </div>
  </header>

  <h1 class="abs headline">The<br>Next<br><span class="accent">Discovery</span><br>Is them<span class="accent">.</span></h1>
  <div class="abs headline-rule"></div>
  <p class="abs tagline">Exploring how emotions, decisions, and puberty shape adolescent brain development.</p>

  <div class="abs side-words">BRAIN • MIND • GROWTH</div>

  <div class="abs comp-ring"></div>
  <div class="abs compensation">
    <svg width="32" height="20" viewBox="0 0 32 20" fill="none" stroke="#fff" stroke-width="1.4"><rect x="1" y="2" width="30" height="16" rx="1"/><circle cx="16" cy="10" r="4"/></svg>
    <div class="label">COMPENSATION<br>UP TO</div>
    <div class="amount">$140</div>
  </div>

  <section class="abs audience-band"></section>
  <div class="abs icon-ring audience-icon">
    <svg width="48" height="40" viewBox="0 0 48 40" fill="none" stroke="#2fc0bd" stroke-width="1.6"><circle cx="17" cy="11" r="7"/><path d="M3 36c0-9 6-14 14-14s14 5 14 14z"/><circle cx="34" cy="15" r="5.5"/><path d="M30 26c2-1 3-1 4-1 6 0 10 4 10 11H33"/></svg>
  </div>
  <div class="abs audience-q">ARE YOU THE PARENT OF A</div>
  <div class="abs audience-age">CHILD AGE 10–17?</div>
  <div class="abs band-divider"></div>
  <div class="abs audience-worry">Do they worry or<br>overthink negative<br>emotions<span class="q">?</span></div>

  <section class="abs involve-panel"></section>
  <h2 class="abs involve-title">STUDY PARTICIPATION INVOLVES:</h2>

  <div class="abs step" style="top:797px">
    <div class="step-icon" style="background:var(--purple)">
      <svg width="28" height="24" viewBox="0 0 28 24" fill="none" stroke="#fff" stroke-width="1.6"><rect x="2" y="2" width="24" height="15" rx="4"/><path d="M10 17l4 5 4-5"/><circle cx="9" cy="9.5" r="1"/><circle cx="14" cy="9.5" r="1"/><circle cx="19" cy="9.5" r="1"/></svg>
    </div>
    <div><div class="step-name" style="color:var(--purple)">One one-hour interview</div><div class="step-text">(online or in-person) where your child will discuss their thoughts</div></div>
  </div>
  <div class="abs step-rule" style="top:867px"></div>

  <div class="abs step" style="top:865px">
    <div class="step-icon" style="background:var(--teal)">
      <svg width="24" height="28" viewBox="0 0 24 28" fill="none" stroke="#1b1f3a" stroke-width="1.6"><rect x="2" y="4" width="20" height="22" rx="2"/><rect x="8" y="1" width="8" height="5" rx="1"/><path d="M6 12l1.5 1.5L10 11M6 18l1.5 1.5L10 17M13 12h6M13 18h6"/></svg>
    </div>
    <div style="padding-top:12px"><div class="step-name" style="color:var(--teal)">Online questionnaires</div><div class="step-text">(parent and child)</div></div>
  </div>
  <div class="abs step-rule" style="top:923px"></div>

  <div class="abs step" style="top:933px">
    <div class="step-icon" style="background:var(--purple-band)">
      <svg width="30" height="26" viewBox="0 0 30 26" fill="none" stroke="#fff" stroke-width="1.5"><path d="M4 22V13a11 11 0 0 1 22 0v9z"/><circle cx="15" cy="13" r="5"/><path d="M2 24h26"/></svg>
    </div>
    <div><div class="step-name" style="color:var(--purple-deep)">One two-hour visit</div><div class="step-text">where your child will complete an MRI scan, answer questions about their puberty stage, and have a small hair sample taken to study puberty hormones</div></div>
  </div>

  <h2 class="abs eligible-title">Your child may be<br>eligible if they:</h2>
  <div class="abs eligible-rule"></div>
  <ul class="abs criteria">
    <li><svg width="20" height="20" viewBox="0 0 20 20" fill="none" stroke="#2fc0bd" stroke-width="1.4"><circle cx="10" cy="10" r="9"/><path d="M6 10l3 3 5-6"/></svg>Are age 10–17</li>
    <li><svg width="20" height="20" viewBox="0 0 20 20" fill="none" stroke="#2fc0bd" stroke-width="1.4"><circle cx="10" cy="10" r="9"/><path d="M6 10l3 3 5-6"/></svg>Tend to worry or overthink negative thoughts</li>
    <li><svg width="20" height="20" viewBox="0 0 20 20" fill="none" stroke="#2fc0bd" stroke-width="1.4"><circle cx="10" cy="10" r="9"/><path d="M6 10l3 3 5-6"/></svg>Have not been diagnosed with psychosis, learning problems, or autism</li>
  </ul>

  <div class="abs scan-image" role="img" aria-label="Coronal brain MRI scan in cool blue tones"></div>

  <section class="abs contact-band"></section>
  <div class="abs icon-ring contact-icon">
    <svg width="28" height="20" viewBox="0 0 28 20" fill="none" stroke="#fff" stroke-width="1.5"><rect x="1" y="1" width="26" height="18" rx="1"/><path d="M1 2l13 10 13-10M1 19l10-9M27 19l-10-9"/></svg>
  </div>
  <div class="abs contact-copy">
    <div class="a">INTERESTED IN PARTICIPATING?</div>
    <div class="b">WANT MORE INFORMATION?</div>
    <div class="c">Please contact us!</div>
  </div>
  <div class="abs contact-divider"></div>
  <div class="abs contact-email">briskstudy@northvale.edu</div>
  <div class="abs email-rule"></div>

  <footer class="abs footer"></footer>
  <div class="abs institution">
    <div class="institution-mark"></div>
    <div class="institution-name">Northvale<br>University</div>
  </div>
  <div class="abs foot-divider" style="left:263px"></div>
  <div class="abs foot-icon" style="left:281px;top:1134px">
    <svg width="44" height="50" viewBox="0 0 44 50" fill="none" stroke="#2fc0bd" stroke-width="1.6"><path d="M22 3l17 6v13c0 12-8 20-17 24C13 42 5 34 5 22V9z"/><path d="M14 24l6 6 11-12"/></svg>
  </div>
  <p class="abs foot-text" style="left:337px;top:1134px">This study is conducted by<br>researchers at Northvale<br>University. All information<br>is kept confidential.</p>
  <div class="abs foot-divider" style="left:523px"></div>
  <div class="abs icon-ring foot-icon" style="left:548px;top:1135px">
    <svg width="20" height="24" viewBox="0 0 20 24" fill="none" stroke="#2fc0bd" stroke-width="1.6"><rect x="2" y="10" width="16" height="12" rx="1.5"/><path d="M5 10V7a5 5 0 0 1 10 0v3M10 15v3"/></svg>
  </div>
  <p class="abs foot-text" style="left:617px;top:1140px">Your child's safety<br>and comfort are<br>our top priority.</p>
</main>
</body>
</html>
```